Acupuncture business needs business card design

I need a business card for an acupuncture clinic called "Harbour Balance"
It will need the following details:
My name: Mark Tevita
Acupuncturist
Member KPTG
WFB Treatment Provider
Ph numbers: 512 8830 027 584 1176
Email: mark@hbneedle.example.nz
On the back it will need a table with 2 columns for appointments, one column for time and one for date.

Industry/Entity Type

Clinic

Contact Information for Business Card

Mark Tevita
Acupuncturist
Member KPTG
WFB Treatment Provider
Email: mark@hbneedle.example.nz

Requirements
Must have
• Mark Tevita
• Acupuncturist
• Member KPTG
• WFB Treatment Provider
• Ph numbers: 512 8830 027 584 1176
• Email: mark@hbneedle.example.nz
• On the back it will need a table with 2 columns for appointments, one column for time and one for date.

```html
<!DOCTYPE html>
<html lang="en">
<head>
<meta charset="utf-8">
<title>Harbour Balance – Business Card</title>
<link rel="stylesheet" href="https://fonts.googleapis.com/css2?family=Exo+2:wght@400;500&family=Roboto:wght@400;500&display=swap">
<style>
  :root {
    --page-bg: #e9ecee;
    --card-bg: #fbfcfc;
    --teal: #2a9fc0;
    --teal-dark: #1d7f9c;
    --teal-light: #7fc7da;
    --rule: #bfe0ea;
    --ink: #2b2f33;
    --ink-soft: #4a5055;
  }
  * { box-sizing: border-box; margin: 0; padding: 0; }
  html, body {
    width: 1200px; height: 899px; overflow: hidden;
    background: var(--page-bg);
  }
  .card {
    position: absolute; left: 270px;
    width: 660px; height: 378px;
    background: var(--card-bg);
    border-radius: 32px;
    overflow: hidden;
    box-shadow: 0 8px 24px rgba(0,0,0,0.12);
    font-family: "Roboto", Arial, sans-serif;
  }
  .card-front { top: 46px; }
  .card-back { top: 468px; }

  .brand { text-align: center; }
  .brand-mark {
    width: 26px; height: 26px; border-radius: 50%;
    background: var(--teal); margin: 0 auto 10px;
  }
  .brand-name {
    font-size: 31px; font-weight: 500; color: var(--teal);
    letter-spacing: -0.4px; white-space: nowrap; line-height: 1.1;
  }
  .brand-tagline {
    margin-top: 4px;
    font-size: 9.5px; letter-spacing: 3.2px; color: var(--teal-light);
    text-transform: uppercase; white-space: nowrap;
  }
  .card-front .brand { position: absolute; left: 36px; top: 112px; width: 300px; }

  .details { position: absolute; left: 362px; top: 46px; color: var(--ink); }
  .person-name {
    font-family: "Exo 2", sans-serif; font-size: 21px; font-weight: 500;
    letter-spacing: 1.6px; color: var(--teal-dark); text-transform: uppercase;
  }
  .person-role {
    font-family: "Exo 2", sans-serif; font-size: 15px; color: var(--ink-soft);
    margin-top: 2px;
  }
  .credentials {
    font-family: "Exo 2", sans-serif; font-size: 15.5px; line-height: 1.35;
    margin-top: 24px; color: var(--ink);
  }
  .contact-list { list-style: none; margin-top: 20px; }
  .contact-list li {
    display: flex; align-items: center; gap: 11px;
    font-family: "Exo 2", sans-serif; font-size: 13px; color: var(--ink-soft);
    height: 22px;
  }
  .contact-list svg { width: 13px; height: 13px; fill: var(--ink-soft); flex: none; }

  .footer-band { position: absolute; left: 0; bottom: 0; width: 660px; height: 118px; }
  .website {
    position: absolute; left: 142px; bottom: 24px;
    font-family: "Exo 2", sans-serif; font-size: 13.5px; letter-spacing: 2px;
    color: #ffffff; transform: rotate(-2deg);
  }

  .card-back .brand { position: absolute; left: 0; top: 34px; width: 660px; }
  .card-back .brand-mark { display: none; }
  .appointments {
    position: absolute; left: 110px; top: 128px; width: 440px;
    border-collapse: collapse;
    font-family: "Exo 2", sans-serif; color: var(--ink-soft);
  }
  .appointments caption {
    font-size: 13px; letter-spacing: 2px; text-transform: uppercase;
    color: var(--teal-dark); padding-bottom: 8px;
  }
  .appointments th {
    font-weight: 500; font-size: 14px; color: #ffffff;
    background: var(--teal); height: 28px; width: 50%;
  }
  .appointments td {
    height: 36px; border-bottom: 1px solid var(--rule);
  }
  .appointments td + td, .appointments th + th { border-left: 1px solid var(--rule); }
</style>
</head>
<body>
  <section class="card card-front">
    <div class="brand">
      <div class="brand-mark"></div>
      <div class="brand-name">Harbour Balance</div>
      <div class="brand-tagline">Acupuncture Physiotherapy</div>
    </div>

    <div class="details">
      <div class="person-name">Mark Tevita</div>
      <div class="person-role">Acupuncturist</div>
      <div class="credentials">Member KPTG<br>WFB Treatment Provider</div>
      <ul class="contact-list">
        <li>
          <svg viewBox="0 0 16 16"><path d="M3.5 1.5l2.5 0 1.2 3-1.6 1.2c.8 1.8 2.2 3.2 4 4l1.2-1.6 3 1.2v2.5c0 .9-.8 1.7-1.7 1.6C6.9 12.9 3.1 9.1 1.9 3.2 1.8 2.3 2.6 1.5 3.5 1.5z"/></svg>
          512 8830
        </li>
        <li>
          <svg viewBox="0 0 16 16"><path d="M4.5 1h7c.6 0 1 .4 1 1v12c0 .6-.4 1-1 1h-7c-.6 0-1-.4-1-1V2c0-.6.4-1 1-1zm.8 2v9h5.4V3H5.3zM8 12.6a.8.8 0 100 1.6.8.8 0 000-1.6z"/></svg>
          027 584 1176
        </li>
        <li>
          <svg viewBox="0 0 16 16"><path d="M1 3.5h14v9H1zm1.5 1.2V5l5.5 4 5.5-4v-.3zm0 2.2v4.4h11V6.9L8 10.8z"/></svg>
          mark@hbneedle.example.nz
        </li>
        <li>
          <svg viewBox="0 0 16 16"><path d="M8 1a7 7 0 100 14A7 7 0 008 1zm0 1.5c.8 0 1.7 1.6 2 4H6c.3-2.4 1.2-4 2-4zM6 8h4c-.1 2.9-1.1 5.5-2 5.5S6.1 10.9 6 8zM2.6 7.2a5.5 5.5 0 012.9-4.1c-.5 1-.9 2.4-1 4.1H2.6zm8.9 0c-.1-1.7-.5-3.1-1-4.1a5.5 5.5 0 012.9 4.1h-1.9zM2.6 8.8h1.9c.1 1.7.5 3.1 1 4.1a5.5 5.5 0 01-2.9-4.1zm8.9 0h1.9a5.5 5.5 0 01-2.9 4.1c.5-1 .9-2.4 1-4.1z"/></svg>
          www.harbourbalance.example
        </li>
      </ul>
    </div>

    <svg class="footer-band" viewBox="0 0 840 150" preserveAspectRatio="none" aria-hidden="true">
      <path d="M0 40 C 220 55, 520 95, 840 150 L 0 150 Z" fill="var(--teal-light)" opacity="0.55"/>
      <path d="M0 55 C 230 65, 500 100, 800 150 L 0 150 Z" fill="var(--teal)"/>
      <path d="M0 120 C 200 115, 420 125, 620 150 L 0 150 Z" fill="var(--teal-dark)" opacity="0.35"/>
    </svg>
    <div class="website">www.harbourbalance.example</div>
  </section>

  <section class="card card-back">
    <div class="brand">
      <div class="brand-mark"></div>
      <div class="brand-name">Harbour Balance</div>
      <div class="brand-tagline">Acupuncture Physiotherapy</div>
    </div>
    <table class="appointments">
      <caption>Your Appointments</caption>
      <thead>
        <tr><th>Date</th><th>Time</th></tr>
      </thead>
      <tbody>
        <tr><td></td><td></td></tr>
        <tr><td></td><td></td></tr>
        <tr><td></td><td></td></tr>
        <tr><td></td><td></td></tr>
        <tr><td></td><td></td></tr>
      </tbody>
    </table>
  </section>
</body>
</html>
```